Car Waterless Cleaner 4 in 1 (100% Natural) Clean, Shine, Protect; Water Repellent. High Eff...

We need to design labels for our Car Care & Cleaning products,
Labels on both 500 ml Bottle Spray sides (text will be provided).
5 and 10 liters Car Shampoo.

I need you to come with Car necessary images (Shining cars, Leather car seats ...)

We are a manufacturer of innovative Green Cleaning products; made with green plants and grain extract, (Leather Cleaner & Conditioner, Multi purpuses Cleaner, Car Shine Polish, car Shampoo)

Target Market(s)

Car Care & Cleaning products, Car Dealer, Car Collectors.

Logo Text

No Idea yet, lol, ;) "Car Tovarex Plume" may be?

Font styles to use
Serif

Requirements
Must have
• Similar projects, Inoovative, Comprehencive, good expertise.

```html
<!DOCTYPE html>
<html lang="en">
<head>
<meta charset="utf-8">
<title>Waterless Car Wash &amp; Rain Repellent – 500 ml Label</title>
<link rel="stylesheet" href="https://fonts.googleapis.com/css2?family=Montserrat:wght@700;800&family=Oswald:wght@500;600&family=Barlow+Condensed:ital,wght@1,600&family=Roboto+Condensed:wght@700&display=swap">
<style>
  :root {
    --navy: #0f2a8c;
    --ink: #111827;
    --lime: #bcd64a;
    --gold: #c9a227;
    --red: #e0200e;
    --brown: #5a1c0c;
    --badge-brown: #5e2410;
    --tick-green: #2e9b2a;
    --leaf-green: #6fb83a;
    --blue-deep: #0b6fd8;
    --blue-light: #2e8df0;
    --white: #ffffff;
  }
  * { box-sizing: border-box; margin: 0; padding: 0; }
  html, body { width: 880px; height: 1200px; overflow: hidden; background: #fff; }
  .label {
    position: relative;
    width: 880px;
    height: 1200px;
    overflow: hidden;
    font-family: "Montserrat", sans-serif;
  }
  .backdrop {
    position: absolute; inset: 0;
    background:
      radial-gradient(ellipse at 55% 30%, #eaf1f5 0%, rgba(200,220,232,0.6) 35%, transparent 60%),
      radial-gradient(ellipse at 5% 20%, #5f9a5a 0%, transparent 35%),
      radial-gradient(ellipse at 10% 75%, #4f8d4a 0%, transparent 30%),
      radial-gradient(ellipse at 90% 85%, #6aa060 0%, transparent 30%),
      linear-gradient(180deg, #8fb3c8 0%, #b9d0dc 40%, #a9c4d2 70%, #8eb1c2 100%);
  }
  .shapes { position: absolute; inset: 0; }
  .name-band {
    position: absolute; left: 0; top: 396px; width: 880px; height: 174px;
    background: rgba(236, 243, 247, 0.82);
  }
  .logo-text {
    position: absolute; left: 200px; top: 166px;
    font-weight: 800; font-size: 106px; line-height: 96px;
    color: var(--navy); letter-spacing: 1px;
  }
  .new-tag {
    position: absolute; left: 658px; top: 170px; width: 222px; height: 108px;
    background: var(--red); border-radius: 44px 0 0 44px;
    color: var(--white); font-weight: 800; font-size: 50px;
    display: flex; align-items: center; justify-content: center; padding-right: 4px;
  }
  .product-name {
    position: absolute; left: 204px; top: 422px; width: 480px; text-align: center;
    font-weight: 700; font-size: 76px; line-height: 1; color: var(--navy);
    letter-spacing: -1px; white-space: nowrap;
    text-shadow: 0 0 3px #fff, 0 0 3px #fff;
  }
  .product-sub {
    position: absolute; left: 204px; top: 496px; width: 474px; text-align: center;
    font-family: "Oswald", sans-serif; font-weight: 500; font-size: 40px; line-height: 1;
    color: var(--ink); letter-spacing: -0.6px; white-space: nowrap;
    text-shadow: 0 0 3px #fff, 0 0 3px #fff;
  }
  .photo {
    position: absolute; border: 4px solid var(--white);
    box-shadow: 0 4px 12px rgba(0,0,0,0.3);
    transform: rotate(-7deg);
  }
  .photo--towel { left: 70px; top: 594px; width: 310px; height: 188px;
    background: linear-gradient(135deg, #e9edf2 0%, #cfd6df 45%, #2f7fd6 60%, #d6dbe2 100%); }
  .photo--seats { left: 283px; top: 690px; width: 330px; height: 186px;
    background: linear-gradient(160deg, #c9b27a 0%, #3a3430 35%, #a8663c 60%, #6b3a22 100%); }
  .photo--car { left: 68px; top: 805px; width: 330px; height: 198px;
    background: linear-gradient(150deg, #6a6a6a 0%, #d11a18 30%, #b8120f 65%, #3d3d3d 100%); }
  .badge { position: absolute; left: 582px; top: 598px; width: 222px; height: 222px; }
  .benefits {
    position: absolute; left: 498px; top: 876px; list-style: none;
  }
  .benefits li {
    display: flex; align-items: center; gap: 8px; height: 41.6px;
    font-family: "Oswald", sans-serif; font-weight: 500; font-size: 35px;
    color: var(--ink); white-space: nowrap;
    text-shadow: 0 0 2px #fff, 0 0 2px #fff, 0 0 3px #fff;
  }
  .benefits li span { display: inline-block; transform: scaleX(0.84); transform-origin: left center; letter-spacing: -0.5px; }
  .benefits svg { width: 32px; height: 32px; flex: none; }
  .origin-note {
    position: absolute; left: 118px; top: 1094px;
    font-family: "Barlow Condensed", sans-serif; font-style: italic; font-weight: 600;
    font-size: 27px; line-height: 32px; color: var(--white);
  }
  .volume {
    position: absolute; left: 590px; top: 1110px; width: 290px; height: 90px;
    background: var(--brown); border-radius: 28px 0 0 0;
    color: var(--white); font-family: "Roboto Condensed", sans-serif; font-weight: 700;
    display: flex; align-items: center; justify-content: center; padding-right: 14px;
    font-size: 46px;
  }
  .volume small { font-size: 32px; margin-left: 10px; margin-top: 8px; }
</style>
</head>
<body>
<div class="label">
  <div class="backdrop" role="img" aria-label="Soft water-textured background with green plant leaves"></div>

  <svg class="shapes" width="880" height="1200" viewBox="0 0 880 1200">
    <path d="M548 0 L880 0 L880 900 C 860 560, 760 230, 548 0 Z" fill="var(--lime)"/>
    <path d="M548 0 C 760 230, 860 560, 880 900" fill="none" stroke="var(--gold)" stroke-width="6"/>
    <path d="M0 800 C 220 960, 430 1060, 620 1200 L0 1200 Z" fill="var(--blue-light)"/>
    <path d="M0 830 C 230 1000, 440 1080, 590 1200 L0 1200 Z" fill="var(--blue-deep)"/>
  </svg>

  <div class="name-band"></div>

  <div class="logo-text">YOUR<br>LOGO</div>
  <div class="new-tag">NEW</div>

  <h1 class="product-name">WATERLESS</h1>
  <p class="product-sub">CAR WASH &amp; RAIN REPELLENT</p>

  <div class="photo photo--towel" role="img" aria-label="Hand wiping a white car body with a blue microfiber towel"></div>
  <div class="photo photo--seats" role="img" aria-label="Car interior with tan leather seats"></div>
  <div class="photo photo--car" role="img" aria-label="Shining red luxury car front"></div>

  <svg class="badge" viewBox="0 0 222 222" role="img" aria-label="100% natural organic product seal">
    <defs>
      <path id="arc-top" d="M 45 111 A 66 66 0 0 1 177 111"/>
      <path id="arc-bottom" d="M 28 111 A 83 83 0 0 0 194 111"/>
    </defs>
    <g fill="var(--badge-brown)">
      <circle cx="111" cy="111" r="100"/>
      <circle cx="111" cy="11" r="12"/><circle cx="111" cy="211" r="12"/>
      <circle cx="11" cy="111" r="12"/><circle cx="211" cy="111" r="12"/>
      <circle cx="40" cy="40" r="12"/><circle cx="182" cy="40" r="12"/>
      <circle cx="40" cy="182" r="12"/><circle cx="182" cy="182" r="12"/>
      <circle cx="73" cy="19" r="12"/><circle cx="149" cy="19" r="12"/>
      <circle cx="73" cy="203" r="12"/><circle cx="149" cy="203" r="12"/>
      <circle cx="19" cy="73" r="12"/><circle cx="19" cy="149" r="12"/>
      <circle cx="203" cy="73" r="12"/><circle cx="203" cy="149" r="12"/>
    </g>
    <circle cx="111" cy="111" r="94" fill="var(--white)"/>
    <circle cx="111" cy="111" r="89" fill="none" stroke="var(--badge-brown)" stroke-width="2"/>
    <circle cx="26" cy="111" r="5" fill="var(--badge-brown)"/>
    <circle cx="196" cy="111" r="5" fill="var(--badge-brown)"/>
    <circle cx="111" cy="111" r="44" fill="none" stroke="#d0d0d0" stroke-width="6"/>
    <circle cx="111" cy="111" r="39" fill="var(--leaf-green)"/>
    <text font-family="Oswald, sans-serif" font-weight="600" font-size="19" fill="var(--badge-brown)">
      <textPath href="#arc-top" startOffset="50%" text-anchor="middle">100% NATURAL</textPath>
    </text>
    <text font-family="Oswald, sans-serif" font-weight="600" font-size="19" fill="var(--badge-brown)">
      <textPath href="#arc-bottom" startOffset="50%" text-anchor="middle">ORGANIC PRODUCT</textPath>
    </text>
  </svg>

  <ul class="benefits">
    <li><svg viewBox="0 0 32 32"><rect x="2" y="6" width="24" height="24" fill="#fff" stroke="var(--tick-green)" stroke-width="2.5"/><path d="M7 17 L13 24 L29 3" fill="none" stroke="var(--tick-green)" stroke-width="4" stroke-linecap="round"/></svg><span>TREAT GLASS</span></li>
    <li><svg viewBox="0 0 32 32"><rect x="2" y="6" width="24" height="24" fill="#fff" stroke="var(--tick-green)" stroke-width="2.5"/><path d="M7 17 L13 24 L29 3" fill="none" stroke="var(--tick-green)" stroke-width="4" stroke-linecap="round"/></svg><span>SPRAY ON, WIPE OFF</span></li>
    <li><svg viewBox="0 0 32 32"><rect x="2" y="6" width="24" height="24" fill="#fff" stroke="var(--tick-green)" stroke-width="2.5"/><path d="M7 17 L13 24 L29 3" fill="none" stroke="var(--tick-green)" stroke-width="4" stroke-linecap="round"/></svg><span>APPLIES WATER</span></li>
    <li><svg viewBox="0 0 32 32"><rect x="2" y="6" width="24" height="24" fill="#fff" stroke="var(--tick-green)" stroke-width="2.5"/><path d="M7 17 L13 24 L29 3" fill="none" stroke="var(--tick-green)" stroke-width="4" stroke-linecap="round"/></svg><span>BEADING TECHNOLOGY</span></li>
    <li><svg viewBox="0 0 32 32"><rect x="2" y="6" width="24" height="24" fill="#fff" stroke="var(--tick-green)" stroke-width="2.5"/><path d="M7 17 L13 24 L29 3" fill="none" stroke="var(--tick-green)" stroke-width="4" stroke-linecap="round"/></svg><span>TO ALL SURFACES</span></li>
  </ul>

  <p class="origin-note">Made with green<br>plants and&nbsp; grain extract</p>

  <div class="volume">500<small>ml</small></div>
</div>
</body>
</html>
```